Outdoor Company Business Card design

We are an outdoor adventure company needing a business card. We sell outdoor adventures and clothing. Please use our logo in the business card. We are looking for something unique but delivers a clear message as to who we are. Please be creative

Target Market(s)

Outdoor adventures

Industry/Entity Type

Business

Contact Information for Business Card

Business name: TrailBirch If using the logo, no need to have a spot for the name
Owner / CEO: Ross Dalby
Website: TrailBirch.example
Facebook: Facebook.com/TrailBirch
Instagram: @dalby_ross
phone number: 555-304-7192
Email: Dalbycrew@TrailBirch.example

Colors

Designer to choose colors to be used in the design.

Requirements
Must have
• The business card must include the details mentioned above. ie logo, my name, email, facebook, instagram, website, and phone number.
Should not have
• should not be cluttered or look messy

```html
<!DOCTYPE html>
<html lang="en">
<head>
<meta charset="utf-8">
<title>TrailBirch Business Card</title>
<link rel="stylesheet" href="https://fonts.googleapis.com/css2?family=Montserrat:wght@600&family=Roboto:wght@400&display=swap">
<style>
  :root {
    --backdrop: #a8a8a8;
    --card: #f1f1f1;
    --brand-blue: #2d5ea4;
    --brand-orange: #d24f1e;
    --ink: #2a2a2a;
    --icon-orange: #d9542a;
  }
  * { margin: 0; padding: 0; box-sizing: border-box; }
  html, body { width: 1200px; height: 1138px; overflow: hidden; }
  body { background: var(--backdrop); position: relative; font-family: "Roboto", Arial, sans-serif; color: var(--ink); }

  .card {
    position: absolute;
    width: 620px;
    height: 375px;
    background: var(--card);
    border-radius: 16px;
    box-shadow: 0 3px 6px rgba(0,0,0,0.25);
  }
  .card--front { left: 274px; top: 186px; }
  .card--back  { left: 276px; top: 608px; }

  .wordmark {
    position: absolute;
    font-family: "Montserrat", Arial, sans-serif;
    font-weight: 600;
    color: var(--brand-blue);
    white-space: nowrap;
    line-height: 1;
  }
  .card--front .wordmark { left: 0; right: 0; top: 190px; text-align: center; font-size: 56px; }
  .card--back .wordmark { left: 318px; top: 114px; font-size: 42px; }

  .front-url {
    position: absolute; left: 0; right: 0; top: 348px;
    text-align: center; font-size: 16px;
  }
  .front-url .accent-blue { color: var(--brand-blue); }
  .front-url .accent-orange { color: var(--brand-orange); }

  .person { position: absolute; left: 32px; top: 78px; }
  .person__name {
    font-family: "Montserrat", Arial, sans-serif;
    font-weight: 600; font-size: 32px; line-height: 1; letter-spacing: 0.5px;
  }
  .person__name .first { color: var(--brand-blue); }
  .person__name .last { color: var(--brand-orange); }
  .person__role { font-size: 16px; margin-top: 6px; }

  .contact-list { position: absolute; left: 36px; top: 274px; list-style: none; }
  .contact-list li, .social-list li {
    display: flex; align-items: center; height: 24px; font-size: 16.5px;
  }
  .contact-list svg { width: 15px; height: 15px; margin-right: 10px; flex: none; }

  .social-list { position: absolute; left: 480px; top: 298px; list-style: none; }
  .social-dot {
    width: 15px; height: 15px; border-radius: 50%; margin-right: 6px; flex: none;
    background: var(--brand-blue);
  }
  .social-dot--alt { background: var(--brand-orange); }
</style>
</head>
<body>
  <section class="card card--front">
    <div class="wordmark">TrailBirch</div>
    <p class="front-url">www.<span class="accent-blue">Trail</span><span class="accent-orange">Birch</span>.example</p>
  </section>

  <section class="card card--back">
    <div class="person">
      <h1 class="person__name"><span class="first">ROSS</span> <span class="last">DALBY</span></h1>
      <p class="person__role">Owner / CEO</p>
    </div>

    <div class="wordmark">TrailBirch</div>

    <ul class="contact-list">
      <li>
        <svg viewBox="0 0 16 16" aria-hidden="true"><path fill="var(--icon-orange)" d="M2 5c0-2 2-3 6-3s6 1 6 3v1h-3V5H5v1H2z M4 7h8l2 7H2z"/></svg>
        555-304-7192
      </li>
      <li>
        <svg viewBox="0 0 16 16" aria-hidden="true"><rect x="1" y="3" width="14" height="10" fill="var(--icon-orange)"/><path d="M1 3l7 6 7-6" fill="none" stroke="#f1f1f1" stroke-width="1.4"/></svg>
        www.TrailBirch.example
      </li>
      <li>
        <svg viewBox="0 0 16 16" aria-hidden="true"><g fill="none" stroke="var(--icon-orange)" stroke-width="1.4"><circle cx="8" cy="8" r="6.3"/><ellipse cx="8" cy="8" rx="2.8" ry="6.3"/><path d="M1.7 8h12.6M3 4.5h10M3 11.5h10"/></g></svg>
        Dalbycrew@TrailBirch.example
      </li>
    </ul>

    <ul class="social-list">
      <li><span class="social-dot"></span>/TrailBirch</li>
      <li><span class="social-dot social-dot--alt"></span>@dalby_ross</li>
    </ul>
  </section>
</body>
</html>
```